Picture Ads

We need some banner ads for our home business opportunity, we are evolving from text to picture ads. I have added some examples of what other distributors are using. We are looking for something really eye catching with some good key words and nice bright colours and to include our photo (attached)
Key words to include:
Booming online business
Personal Development and Leadership Industry
Earn an executive income from home
Simple 3 step system
Make up to $5,000 per sale
Not MLM
The size needs to be: 1000 x 35 pixels
13.9 x 4.75 Inches
35.3 x 11.1 cm
I think different platforms accept different sizes, not too familiar with it yet, any guidance welcome. I've clicked project for 2 days if that is to prioritise the order?
Many thanks,
Maren

Industry/Entity Type

Business

```html
<!DOCTYPE html>
<html lang="en">
<head>
<meta charset="utf-8">
<title>Booming Online Business – Banner</title>
<link rel="stylesheet" href="https://fonts.googleapis.com/css2?family=Chewy&family=Gelasio:wght@400;500&family=Caveat:wght@500&display=swap">
<style>
  :root {
    --sky: #29aee6;
    --lime: #5af21e;
    --sun: #f4f50c;
    --magenta: #e52bd0;
    --orange: #f7610f;
    --red: #ee2a2a;
    --leaf: #63ee28;
    --lemon: #e9f81b;
    --paper: #ffffff;
    --ink: #2a2a2a;
    --button-red: #b3191d;
    --button-shadow: #8a8a8a;
    --button-edge: #c8c8c8;
    --button-top: #ffffff;
    --button-bottom: #dcdcdc;
    --photo-dark: #3b2a22;
    --photo-warm: #b9785a;
  }
  html, body {
    margin: 0;
    padding: 0;
    width: 1200px;
    height: 420px;
    overflow: hidden;
    background: var(--paper);
  }
  .banner {
    display: block;
    width: 1200px;
    height: 420px;
  }
  .headline {
    font-family: "Chewy", cursive;
    font-size: 58px;
    fill: var(--paper);
  }
  .selling-point {
    font-family: "Gelasio", serif;
    font-size: 21px;
    fill: var(--paper);
  }
  .caption {
    font-family: "Caveat", cursive;
    font-size: 17px;
    fill: var(--ink);
  }
  .cta-label {
    font-family: "Gelasio", serif;
    font-size: 19px;
    fill: var(--button-red);
  }
</style>
</head>
<body>
<svg class="banner" viewBox="0 0 1000 350" xmlns="http://www.w3.org/2000/svg">
  <defs>
    <linearGradient id="photo-tone" x1="0" y1="0" x2="1" y2="1">
      <stop offset="0" stop-color="var(--photo-dark)"/>
      <stop offset="0.55" stop-color="var(--photo-warm)"/>
      <stop offset="1" stop-color="var(--photo-dark)"/>
    </linearGradient>
    <linearGradient id="button-face" x1="0" y1="0" x2="0" y2="1">
      <stop offset="0" stop-color="var(--button-top)"/>
      <stop offset="1" stop-color="var(--button-bottom)"/>
    </linearGradient>
  </defs>

  <!-- background fields -->
  <rect class="field-sky" x="270" y="0" width="730" height="280" fill="var(--sky)"/>
  <rect class="field-sun" x="0" y="275" width="1000" height="75" fill="var(--sun)"/>
  <rect class="field-edge" x="0" y="240" width="14" height="60" fill="var(--sky)"/>
  <path class="blob-right" d="M1000,20 C900,0 820,70 770,150 C730,205 675,225 660,280 L1000,280 Z" fill="var(--lime)"/>
  <path class="blob-top-left" d="M200,0 L290,0 L290,40 C260,25 230,15 200,0 Z" fill="var(--lime)"/>
  <path class="blob-bottom-left" d="M0,300 C40,295 90,320 120,350 L0,350 Z" fill="var(--lime)"/>

  <!-- confetti dots -->
  <g class="dots">
    <circle cx="327" cy="35" r="33" fill="var(--magenta)"/>
    <circle cx="408" cy="44" r="19" fill="var(--orange)"/>
    <circle cx="479" cy="18" r="11" fill="var(--magenta)"/>
    <circle cx="389" cy="90" r="11" fill="var(--red)"/>
    <circle cx="338" cy="100" r="25" fill="var(--leaf)"/>
    <circle cx="303" cy="170" r="20" fill="var(--lemon)"/>
  </g>

  <!-- portrait card -->
  <g class="portrait-card">
    <rect x="8" y="2" width="272" height="338" fill="var(--paper)"/>
    <rect class="portrait-photo" x="20" y="12" width="248" height="283" fill="url(#photo-tone)"
          role="img" aria-label="Photo of the two business owners smiling together"/>
    <text class="caption" x="144" y="318" text-anchor="middle">Maren and Ilse Corbett</text>
  </g>

  <!-- message -->
  <text class="headline" x="437" y="103" textLength="478" lengthAdjust="spacingAndGlyphs">BOOMING ONLINE BUSINESS!!</text>
  <g class="selling-points" text-anchor="middle">
    <text class="selling-point" x="673" y="148" textLength="430" lengthAdjust="spacingAndGlyphs">EARN AN EXECUTIVE INCOME AT HOME</text>
    <text class="selling-point" x="673" y="175" textLength="590" lengthAdjust="spacingAndGlyphs">PERSONAL DEVELOPMENT AND LEADERSHIP INDUSTRY</text>
    <text class="selling-point" x="673" y="203" textLength="306" lengthAdjust="spacingAndGlyphs">SIMPLE 3 STEP SYSTEM</text>
    <text class="selling-point" x="642" y="230" textLength="312" lengthAdjust="spacingAndGlyphs">MAKE UP TO $5000 PER SALE</text>
    <text class="selling-point" x="649" y="257" textLength="194" lengthAdjust="spacingAndGlyphs">NOT AN MLM</text>
  </g>

  <!-- call to action -->
  <g class="cta-button">
    <rect x="403" y="296" width="400" height="46" rx="3" fill="var(--button-shadow)"/>
    <rect x="400" y="293" width="398" height="44" rx="3" fill="url(#button-face)" stroke="var(--button-edge)"/>
    <text class="cta-label" x="603" y="325" text-anchor="middle" textLength="303" lengthAdjust="spacingAndGlyphs">CLICK HERE FOR MORE DETAILS</text>
  </g>
</svg>
</body>
</html>
```